Real Estate Investment Company Needs A Business Card Designed

I need a business card designed for my use. We are a real estate investment company based in Omaha, Nebraska that specializes in buying, rehabbing and selling single family and multifamily properties. Would love designs that incorporate our logo and colors

Industry/Entity Type

Business

Contact Information for Business Card

Mitchell Parkhurst | President & CEO
4873 North 52nd Avenue, Ste 700
Omaha, NE 68142
(402) 786-4259
mitchell@kestrelgateproperties.example
www.KestrelgateProperties.example

Font styles to use
Serif

Colors
0255a3
3276b5

Requirements
Must have
• Our logo

```html
<!DOCTYPE html>
<html lang="en">
<head>
<meta charset="utf-8">
<title>Kestrelgate Properties – Business Card</title>
<link href="https://fonts.googleapis.com/css2?family=Roboto:wght@400;500&display=swap" rel="stylesheet">
<style>
  :root {
    --bg: #a39c9b;
    --card-white: #ffffff;
    --blue-main: #0280c8;
    --blue-deep: #0566a0;
    --blue-back: #2b78c2;
    --ink-light: #ffffff;
    --brand-blue: #0255a3;
  }
  * { box-sizing: border-box; margin: 0; padding: 0; }
  html, body {
    width: 1200px; height: 1200px; overflow: hidden;
    background: var(--bg);
    font-family: "Roboto", Arial, sans-serif;
  }
  .sheet {
    position: relative; width: 1200px; height: 1200px;
  }
  .card {
    position: absolute; left: 150px; width: 900px; height: 514px;
    overflow: hidden;
    box-shadow: 0 6px 18px rgba(0,0,0,0.25);
  }
  .card--front { top: 57px; background: var(--card-white); }
  .card--back { top: 628px; background: var(--blue-back); }

  .front-shapes { position: absolute; inset: 0; width: 100%; height: 100%; }

  .brand {
    position: absolute; display: flex; flex-direction: column; align-items: center;
    font-weight: 500; text-align: center;
  }
  .brand__mark {
    width: 120px; height: 120px; border-radius: 50%;
    margin-bottom: 22px;
  }
  .brand__name { font-size: 38px; letter-spacing: 1px; line-height: 1; }
  .brand__sub { font-size: 17px; letter-spacing: 4px; margin-top: 8px; line-height: 1; }

  .card--front .brand { left: 30px; width: 330px; top: 160px; color: var(--blue-main); }
  .card--front .brand__mark { background: var(--blue-main); }
  .card--front .brand__name { font-size: 32px; }
  .card--front .brand__sub { font-size: 15px; }

  .card--back .brand { left: 0; right: 0; top: 130px; color: var(--ink-light); }
  .card--back .brand__mark { background: var(--ink-light); }

  .contact {
    position: absolute; right: 38px; top: 96px;
    color: var(--ink-light); text-align: right;
    list-style: none;
  }
  .contact__row { display: flex; justify-content: flex-end; align-items: center; gap: 14px; }
  .contact__row + .contact__row { margin-top: 26px; }
  .contact__text { font-size: 19px; line-height: 1.35; }
  .contact__name { font-size: 32px; font-weight: 400; line-height: 1.1; }
  .contact__title { font-size: 19px; font-weight: 500; }
  .icon { width: 26px; height: 26px; flex: none; }
  .icon path, .icon circle, .icon rect, .icon ellipse, .icon line {
    fill: none; stroke: var(--ink-light); stroke-width: 1.8; stroke-linecap: round; stroke-linejoin: round;
  }
  .icon .solid { fill: var(--ink-light); stroke: none; }
</style>
</head>
<body>
<main class="sheet">

  <section class="card card--front" aria-label="Business card front">
    <svg class="front-shapes" viewBox="0 0 900 514" preserveAspectRatio="none" aria-hidden="true">
      <polygon points="720,0 900,0 900,514 387,514 297,134" fill="var(--blue-main)"/>
      <polygon points="297,134 387,514 612,514" fill="var(--blue-deep)"/>
    </svg>

    <div class="brand">
      <span class="brand__mark" aria-hidden="true"></span>
      <span class="brand__name">KESTRELGATE</span>
      <span class="brand__sub">PROPERTIES</span>
    </div>

    <ul class="contact">
      <li class="contact__row">
        <div class="contact__text">
          <div class="contact__name">Mitchell Parkhurst</div>
          <div class="contact__title">President &amp; CEO</div>
        </div>
        <svg class="icon" viewBox="0 0 24 24" aria-hidden="true">
          <circle cx="12" cy="8" r="4.5"/><path d="M4 22c0-4.5 3.5-7.5 8-7.5s8 3 8 7.5z"/>
        </svg>
      </li>
      <li class="contact__row">
        <span class="contact__text">(402) 786-4259</span>
        <svg class="icon" viewBox="0 0 24 24" aria-hidden="true">
          <path class="solid" d="M6.6 3.5l3 3.3-1.8 2.3c1.3 2.7 3.4 4.8 6.1 6.1l2.3-1.8 3.3 3-2 3.1C11 19.5 4.5 13 3.5 5.5z"/>
        </svg>
      </li>
      <li class="contact__row">
        <span class="contact__text">mitchell@kestrelgateproperties.example</span>
        <svg class="icon" viewBox="0 0 24 24" aria-hidden="true">
          <rect x="3" y="6" width="18" height="13" rx="1"/><path d="M3 7l9 7 9-7"/>
        </svg>
      </li>
      <li class="contact__row">
        <span class="contact__text">4873 North 52nd Avenue, Ste 700<br>Omaha, NE 68142</span>
        <svg class="icon" viewBox="0 0 24 24" aria-hidden="true">
          <path class="solid" d="M12 2a7 7 0 0 0-7 7c0 5 7 13 7 13s7-8 7-13a7 7 0 0 0-7-7zm0 10a3 3 0 1 1 0-6 3 3 0 0 1 0 6z"/>
        </svg>
      </li>
      <li class="contact__row">
        <span class="contact__text">www.KestrelgateProperties.example</span>
        <svg class="icon" viewBox="0 0 24 24" aria-hidden="true">
          <circle cx="12" cy="12" r="9"/><ellipse cx="12" cy="12" rx="4" ry="9"/><line x1="3" y1="12" x2="21" y2="12"/>
        </svg>
      </li>
    </ul>
  </section>

  <section class="card card--back" aria-label="Business card back">
    <div class="brand">
      <span class="brand__mark" aria-hidden="true"></span>
      <span class="brand__name">KESTRELGATE</span>
      <span class="brand__sub">PROPERTIES</span>
    </div>
  </section>

</main>
</body>
</html>
```